Company folder for engineering company in packaging sector

I look for design a flyer of 6 front pages folded . When you open the 3rd page is the center one (behind the 6th one), the first and second on the left and the forth, fifth on the right.
So I open the first page fro tight to left, then left to right.
The third page must be emotional because when you open the folder is the central one.
I add file movie to show an example of folder
Please check the power point trial.

I add acad lay out to if needed to add .

Target Market(s)

We project and manufacture packaging line (please check the power point file attached

Industry/Entity Type

It Company

Requirements
Must have
• The Logo is already in the file if is needed other images or in vectorial format please specify
Nice to have
• It's possible to add a pocket for adding document (as offer) and space for business card

```html
<!DOCTYPE html>
<html lang="en">
<head>
<meta charset="utf-8">
<title>ALTRA – Company Folder</title>
<link href="https://fonts.googleapis.com/css2?family=Arimo:wght@400;700&display=swap" rel="stylesheet">
<style>
  :root {
    --blue: #1d63b4;
    --blue-frame: #1f5fb0;
    --white: #ffffff;
    --ink: #222a33;
    --grey-band: #ececec;
    --grey-area: #e4e5e7;
    --dash: #6b7077;
  }
  * { margin: 0; padding: 0; box-sizing: border-box; }
  html, body { width: 1200px; height: 565px; overflow: hidden; background: var(--white); }
  body { font-family: "Arimo", Arial, sans-serif; color: var(--ink); }
  .folder { position: relative; width: 1200px; height: 565px; overflow: hidden; }
  .backdrop { position: absolute; inset: 0; }

  /* left panel */
  .pill {
    position: absolute; left: 0; height: 22px;
    background: var(--white); color: var(--blue);
    border-radius: 0 11px 11px 0;
    font-size: 15.5px; line-height: 22px; padding-left: 24px;
    white-space: nowrap;
  }
  .copy { position: absolute; left: 24px; width: 360px; color: var(--white); font-size: 10.6px; line-height: 12.7px; }
  .copy p + p { margin-top: 13px; }
  .segments { position: absolute; left: 14px; top: 446px; list-style: none; color: var(--white); font-size: 10.6px; }
  .segments li { height: 15.6px; line-height: 15.6px; }
  .segments li::before { content: "●"; font-size: 7px; margin-right: 6px; vertical-align: 1px; }

  /* panel headings */
  .panel-title { position: absolute; display: flex; align-items: center; font-size: 15px; color: var(--ink); }
  .panel-title .initial {
    width: 19px; height: 19px; border-radius: 50%; background: var(--blue);
    color: var(--white); font-size: 14px; display: flex; align-items: center; justify-content: center; margin-right: 1px;
  }

  .lead { position: absolute; font-size: 10.4px; line-height: 12.7px; color: var(--ink); }
  .dot-item { position: absolute; font-size: 10.4px; color: var(--ink); white-space: nowrap; }
  .dot-item::before { content: "●"; color: var(--blue); font-size: 7px; margin-right: 5px; vertical-align: 1px; }

  .shot { position: absolute; border: 2px solid var(--blue-frame); border-radius: 3px; }
  .shot.steel { background: linear-gradient(160deg, #c9ced4, #7d8793); }
  .shot.dark { background: linear-gradient(160deg, #5a6878, #2b3542); }
  .shot.orange { background: linear-gradient(180deg, #6a7a8c, #d9661f); }
  .caption { position: absolute; font-size: 10.4px; line-height: 13px; color: var(--ink); white-space: nowrap; }

  .layout-plan { position: absolute; left: 829px; top: 286px; width: 356px; height: 187px;
    background: radial-gradient(ellipse at center, #b4b7bb 0%, #cfd1d4 55%, rgba(228,229,231,0) 80%); }

  .brand { position: absolute; right: 4px; top: 531px; font-size: 20px; line-height: 22px; font-weight: 700; color: var(--blue); letter-spacing: 0.5px; white-space: nowrap; }
</style>
</head>
<body>
<div class="folder">
  <svg class="backdrop" width="1200" height="565" viewBox="0 0 1200 565" aria-hidden="true">
    <polygon points="0,0 476,0 336,565 0,565" fill="var(--blue)"/>
    <polygon points="476,0 792,0 792,80 456,80" fill="var(--grey-band)"/>
    <polygon points="802,0 894,0 875,76 802,76" fill="var(--grey-band)"/>
    <polygon points="919,0 1200,0 1200,76 900,76" fill="var(--grey-band)"/>
    <polygon points="870,227 1200,227 1200,556 808,556" fill="var(--grey-area)"/>
    <rect x="339" y="554" width="790" height="9" fill="var(--blue)"/>
    <line x1="402" y1="0" x2="402" y2="565" stroke="var(--dash)" stroke-width="1" stroke-dasharray="9 6"/>
    <line x1="802" y1="0" x2="802" y2="565" stroke="var(--dash)" stroke-width="1" stroke-dasharray="9 6"/>
  </svg>

  <!-- left panel -->
  <div class="pill" style="top:22px; width:108px">Mission</div>
  <div class="copy" style="top:48px">
    <p>To offer integrated solutions for medium and low speed processes,with high technological and quality levels.</p>
    <p>To research &amp; develop innovative solutions that integrate leading-edge Italian competence and expertise in every component of the line.</p>
  </div>

  <div class="pill" style="top:126px; width:153px">History &amp; Values</div>
  <div class="copy" style="top:158px">
    <p>Specialists who have been working together in the field for over 20 years, with countless installations worldwide: ALTRA represents the maximum expression of the experience and competence of its personnel.</p>
    <p>Specialized companies, renown for the excellent quality of their products cooperate to provide customers with integrated solutions, in minimum space requirements and with maximum flexibility.</p>
  </div>

  <div class="pill" style="top:261px; width:121px">What we do</div>
  <div class="copy" style="top:294px; width:340px">
    <p>Our goal is provide the turnkey solution most suited to the specific application.</p>
    <p>We are a committed team and will work in close collaboration with customer personnel responsible for project review, bringing high-level professionalism and competence to each phase of project engineering, from the feasibility analysis to project implementation, during commissioning and start-up, right up to production and beyond, providing full 360° customer service support.</p>
  </div>

  <div class="pill" style="top:418px; width:153px">Market Segment</div>
  <ul class="segments">
    <li>Home &amp; Personal care</li>
    <li>Chemicals</li>
    <li>Foods</li>
    <li>Beverages</li>
    <li>Alcohol &amp; wineries</li>
  </ul>

  <!-- equipment panel -->
  <div class="panel-title" style="left:483px; top:36px"><span class="initial">E</span>quipment</div>
  <div class="lead" style="left:478px; top:89px">The engineering of our equipment are driven by:</div>
  <div class="dot-item" style="left:486px; top:111px">Quality</div>
  <div class="dot-item" style="left:583px; top:111px">Modularity</div>
  <div class="dot-item" style="left:486px; top:135px">Reliability</div>
  <div class="dot-item" style="left:583px; top:135px">Semplicity</div>

  <div class="shot steel" style="left:460px; top:157px; width:90px; height:96px" role="img" aria-label="Photo of a stretch wrapper machine"></div>
  <div class="shot steel" style="left:562px; top:157px; width:90px; height:96px" role="img" aria-label="Photo of a labelling machine"></div>
  <div class="shot dark" style="left:669px; top:157px; width:90px; height:96px" role="img" aria-label="Photo of a handle applicator"></div>
  <div class="caption" style="left:467px; top:257px">Stretch wrapper</div>
  <div class="caption" style="left:587px; top:257px">Labeller</div>
  <div class="caption" style="left:672px; top:257px">Handle applicator</div>

  <div class="shot dark" style="left:460px; top:275px; width:90px; height:97px" role="img" aria-label="Photo of a robot palletizer"></div>
  <div class="shot steel" style="left:562px; top:275px; width:90px; height:97px" role="img" aria-label="Photo of conveyors carrying bottles"></div>
  <div class="shot orange" style="left:669px; top:275px; width:90px; height:97px" role="img" aria-label="Photo of a decrater handling orange canisters"></div>
  <div class="caption" style="left:462px; top:377px">Robot Paletizer &amp;<br>Depaletizer</div>
  <div class="caption" style="left:575px; top:377px">Conveyors &amp;<br>accessories</div>
  <div class="caption" style="left:667px; top:377px">Decraters &amp; Craters</div>

  <div class="caption" style="left:458px; top:432px">Wrap-around</div>
  <div class="shot steel" style="left:524px; top:407px; width:238px; height:51px" role="img" aria-label="Photo of a wrap-around case packer"></div>
  <div class="shot steel" style="left:453px; top:464px; width:206px; height:76px" role="img" aria-label="Photo of a rotary bottle filler"></div>
  <div class="caption" style="left:667px; top:504px">Filler</div>

  <!-- integrated solutions panel -->
  <div class="panel-title" style="left:930px; top:36px"><span class="initial">I</span>ntegrated Solutions</div>
  <div class="lead" style="left:831px; top:89px; width:358px">The market presents us with a series of demands that are notoriously more frequent than others. Precisely in order to meet these market needs, ALTRA has standardized production, permitting us to:</div>
  <div class="dot-item" style="left:866px; top:142px">Reduce our lead time</div>
  <div class="dot-item" style="left:866px; top:168px">Improve the quality of global supply</div>
  <div class="dot-item" style="left:866px; top:192px">Reduce the cost of the investment for our customers</div>

  <div class="layout-plan" role="img" aria-label="Isometric drawing of a packaging line layout with conveyors and machines"></div>

  <div class="brand">ALTRA</div>
</div>
</body>
</html>
```